Postcard Design

I am an attorney in Pittsburgh. Here and across country, companies are sending data with names, address and new criminal charges for people. This has resulted in some people getting 12 or more of these letters. I want to do a postcard because one does not need to open a postcard. I also want to be delicate since there is no sealed envelope. I want to throw in other matters other than criminal so it does not look like the person is necessarily charged with a crime.
At top would be "Law Office of Dennis K. Varholtz"
Then:
Need an Attorney?
Attorney Dennis K. Varholtz has 25 Years of Experience
Free Consultation - Affordable Fees - Credit Cards Accepted
-All Criminal Matters
-Most Civil Matters
-DUI / Traffic Citations / License Restoration
412-555-0187
www.harbordefensecounsel.example
www.dkvcounsel.example

My CTQ ranking is A+ but I am not sure they give a logo with the rating. I have all my logos at www.harbordefensecounsel.example The purpose of the two websites is these are postcards. I want no one to think oh this person is charged with a crime.

```html
<!DOCTYPE html>
<html lang="en">
<head>
<meta charset="utf-8">
<title>Law Office of Dennis K. Varholtz – Postcard</title>
<link rel="stylesheet" href="https://fonts.googleapis.com/css2?family=Crimson+Text:ital,wght@0,400;0,600;0,700;1,400;1,600;1,700&display=swap">
<style>
  :root {
    --page-bg: #e6e7e9;
    --navy-deep: #0b1530;
    --navy: #14264f;
    --blue: #2f5fb8;
    --blue-bright: #3f78d6;
    --red-dark: #7e0a10;
    --orange: #f08a2c;
    --white: #ffffff;
    --ink: #15254c;
    --badge-maroon: #4a1a1f;
    --badge-blue: #1b4a8a;
    --badge-gold: #c9a54a;
  }
  * { box-sizing: border-box; margin: 0; padding: 0; }
  html, body {
    width: 1200px; height: 880px; overflow: hidden;
    background: var(--page-bg);
    font-family: "Crimson Text", Georgia, serif;
    font-variant-ligatures: none;
  }
  .postcard {
    position: absolute; left: 40px; top: 77px;
    width: 1120px; height: 726px;
    overflow: hidden;
    background: linear-gradient(135deg, var(--navy-deep) 0%, var(--navy) 35%, var(--blue) 75%, var(--blue-bright) 100%);
  }
  .postcard__shapes { position: absolute; inset: 0; }
  .office { position: absolute; left: 20px; top: 28px; width: 340px; text-align: center; color: var(--white); }
  .office__label { font-size: 28px; font-weight: 600; line-height: 1.1; }
  .office__name { font-size: 35px; font-weight: 600; color: var(--orange); line-height: 1.15; }
  .office__rule { height: 2px; background: var(--white); opacity: .85; margin: 4px 0 6px; }
  .office__years { font-size: 24px; font-style: italic; font-weight: 600; }
  .practice { position: absolute; left: 36px; top: 220px; list-style: none; color: var(--white); }
  .practice li { position: relative; padding-left: 30px; font-size: 21px; font-weight: 600; line-height: 1.6; }
  .practice li .tick { position: absolute; left: 0; top: 6px; width: 20px; height: 22px; }
  .practice li.practice__wrap { line-height: 1.2; margin-top: 4px; }
  .perks {
    position: absolute; left: 470px; top: 48px; width: 650px; height: 70px;
    display: flex; align-items: center; justify-content: center; gap: 22px;
    color: var(--ink); font-size: 22px; font-weight: 700;
  }
  .perks span::before { content: "•"; margin-right: 8px; }
  .headline {
    position: absolute; left: 330px; top: 118px; width: 790px; height: 149px;
    display: flex; align-items: center; justify-content: center;
    color: var(--white); font-size: 80px; font-style: italic; font-weight: 700;
    letter-spacing: 1px; text-shadow: 0 3px 6px rgba(0,0,0,.45);
  }
  .accreditation {
    position: absolute; right: 40px; top: 470px;
    display: flex; align-items: center; gap: 8px;
    color: var(--white); font-size: 26px; font-weight: 700;
  }
  .accreditation__mark { width: 14px; height: 14px; background: var(--white); }
  .contact { position: absolute; right: 30px; top: 580px; text-align: right; color: var(--white); }
  .contact__phone { font-size: 38px; font-weight: 600; color: var(--orange); letter-spacing: 1px; line-height: 1.2; }
  .contact__web { font-size: 20px; font-weight: 700; line-height: 1.3; }
</style>
</head>
<body>
<div class="postcard">
  <svg class="postcard__shapes" width="1120" height="726" viewBox="0 0 1120 726">
    <defs>
      <linearGradient id="skyBand" x1="0" y1="0" x2="1" y2="0">
        <stop offset="0" stop-color="#8cc4f5"/><stop offset="1" stop-color="#3d7fd8"/>
      </linearGradient>
      <linearGradient id="creamBand" x1="0" y1="0" x2="0" y2="1">
        <stop offset="0" stop-color="#fff8dc"/><stop offset="1" stop-color="#f4dc98"/>
      </linearGradient>
      <linearGradient id="redBand" x1="0" y1="0" x2="0" y2="1">
        <stop offset="0" stop-color="#c8161f"/><stop offset="1" stop-color="#8d0c12"/>
      </linearGradient>
      <linearGradient id="photoTone" x1="0" y1="0" x2="1" y2="1">
        <stop offset="0" stop-color="#3a4a5c"/><stop offset=".45" stop-color="#202a46"/><stop offset="1" stop-color="#2b3f78"/>
      </linearGradient>
      <linearGradient id="lightStripe" x1="0" y1="0" x2="1" y2="0">
        <stop offset="0" stop-color="#dfe8f2"/><stop offset="1" stop-color="#8fb4e6"/>
      </linearGradient>
    </defs>
    <polygon points="488,0 1120,0 1120,48 464,48" fill="url(#skyBand)"/>
    <polygon points="1080,0 1120,0 1120,48 1055,48" fill="#2b5fc4"/>
    <polygon points="464,48 1120,48 1120,118 440,118" fill="url(#creamBand)"/>
    <polygon points="360,118 1120,118 1120,267 312,267" fill="url(#redBand)"/>
    <polygon points="312,267 1120,267 1120,272 310,272" fill="var(--red-dark)"/>
    <polygon points="905,267 938,267 720,726 688,726" fill="url(#lightStripe)"/>
    <g role="img" aria-label="Photo: a police officer seated in a patrol car writing a traffic citation">
      <polygon points="312,267 905,267 688,726 120,726" fill="url(#photoTone)"/>
    </g>
    <g role="img" aria-label="Professional ranking seal">
      <circle cx="120" cy="442" r="72" fill="var(--badge-maroon)"/>
      <circle cx="120" cy="442" r="58" fill="none" stroke="var(--badge-gold)" stroke-width="3"/>
    </g>
    <g role="img" aria-label="Trial lawyers association seal">
      <circle cx="120" cy="602" r="76" fill="var(--badge-blue)"/>
      <circle cx="120" cy="602" r="60" fill="none" stroke="var(--badge-gold)" stroke-width="4"/>
    </g>
  </svg>

  <header class="office">
    <p class="office__label">Law Office of</p>
    <p class="office__name">Dennis K. Varholtz</p>
    <div class="office__rule"></div>
    <p class="office__years">25 years of experience</p>
  </header>

  <ul class="practice">
    <li><svg class="tick" viewBox="0 0 20 22"><path d="M2 12 L8 19 L18 2" fill="none" stroke="var(--orange)" stroke-width="3"/></svg>All Criminal Matters</li>
    <li><svg class="tick" viewBox="0 0 20 22"><path d="M2 12 L8 19 L18 2" fill="none" stroke="var(--orange)" stroke-width="3"/></svg>Most Civil Matters</li>
    <li class="practice__wrap"><svg class="tick" viewBox="0 0 20 22"><path d="M2 12 L8 19 L18 2" fill="none" stroke="var(--orange)" stroke-width="3"/></svg>DUI / Traffic Citations /<br>License Restoration</li>
  </ul>

  <div class="perks">
    <span>Free Consultation</span>
    <span>Affordable Fees</span>
    <span>Credit Cards Accepted</span>
  </div>

  <h1 class="headline">Need an Attorney?</h1>

  <div class="accreditation">
    <span class="accreditation__mark"></span>
    <span>CTQ</span>
  </div>

  <footer class="contact">
    <p class="contact__phone">(412) 555-0187</p>
    <p class="contact__web">www.harbordefensecounsel.example</p>
    <p class="contact__web">www.dkvcounsel.example</p>
  </footer>
</div>
</body>
</html>
```